KRV Ltd Business Card
Professional Biz Card for Kestrel Ridge Ventures IBC Ltd
KRV Ltd Business Card -
Creative Brief
Professional
Milo Harwick
President & CEO
milo@kestrelridgeventures.biz
www.kestrelridgeventures.biz
Skype ID: mharwick should be added.
www.kestrelridgeventures.biz & perhaps a large version of my logo.

```html
<!DOCTYPE html>
<html lang="en">
<head>
<meta charset="utf-8">
<title>KRV Ltd Business Card</title>
<link rel="stylesheet" href="https://fonts.googleapis.com/css2?family=Arimo:wght@400;700&display=swap">
<style>
  :root {
    --stage: #e4e4e4;
    --card: #f4f4f4;
    --card-edge: #fdfdfd;
    --ink: #1a1a1a;
    --ink-soft: #3a3a3a;
    --band: #0d0d0d;
    --band-text: #ffffff;
    --mark: #9a9da1;
  }
  * { margin: 0; padding: 0; box-sizing: border-box; }
  html, body {
    width: 1200px; height: 377px; overflow: hidden;
    background: var(--stage);
    font-family: "Arimo", Arial, sans-serif;
    color: var(--ink);
  }
  .stage { position: relative; width: 1200px; height: 377px; }
  .card {
    position: absolute; top: 24px; width: 560px; height: 330px;
    border-radius: 18px; overflow: hidden;
    background: linear-gradient(180deg, var(--card-edge), var(--card));
    box-shadow: 0 2px 6px rgba(0,0,0,0.18);
  }
  .card-front { left: 30px; }
  .card-back { left: 610px; }

  .front-band {
    position: absolute; top: 0; left: 0; width: 225px; height: 38px;
    background: var(--band); border-bottom-right-radius: 14px;
    display: flex; align-items: center; padding-left: 22px;
  }
  .front-band .url { color: var(--band-text); font-size: 12px; letter-spacing: 0.2px; }
  .front-mark {
    position: absolute; left: 0; right: 0; top: 110px; text-align: center;
    font-size: 110px; font-weight: 700; color: var(--mark); letter-spacing: 6px;
    line-height: 1;
  }

  .holder { position: absolute; left: 34px; top: 58px; }
  .holder .name { font-size: 24px; color: var(--ink); }
  .holder .role { font-size: 12px; color: var(--ink-soft); margin-top: 6px; }
  .back-mark {
    position: absolute; right: 30px; top: 135px;
    font-size: 74px; font-weight: 700; color: var(--mark); letter-spacing: 4px;
    line-height: 1;
  }
  .contact {
    position: absolute; left: 34px; bottom: 26px;
    font-size: 13px; line-height: 1.55; color: var(--ink-soft);
    list-style: none;
  }
  .back-band {
    position: absolute; right: 0; bottom: 0; width: 180px; height: 38px;
    background: var(--band); border-top-left-radius: 14px;
  }
</style>
</head>
<body>
<main class="stage">
  <section class="card card-front" aria-label="Card front">
    <div class="front-band"><span class="url">www.kestrelridgeventures.biz</span></div>
    <div class="front-mark">KRV</div>
  </section>

  <section class="card card-back" aria-label="Card back">
    <div class="holder">
      <p class="name">Milo Harwick</p>
      <p class="role">President &amp; CEO</p>
    </div>
    <div class="back-mark">KRV</div>
    <ul class="contact">
      <li>Cell: +86 139 2045 7716</li>
      <li>Email: milo@kestrelridgeventures.biz</li>
      <li>Skype ID: mharwick</li>
      <li>www.kestrelridgeventures.biz</li>
    </ul>
    <div class="back-band"></div>
  </section>
</main>
</body>
</html>
```